bluecastle aquatics business card

I need a new attractive business card. I am planning on printing on very thick rounded corner stock and having painted edges. We are a swimming pool remodel, repair, and service company in north florida. Our current logo is red, white, and blue. It doesn't necessarily have to stay that way, I am open to other ideas. It will need to contain my name, work and cell numbers, email, website, and my contractor license number.

Target Market(s)

High end residential and commercial clients

Industry/Entity Type

Business

Contact Information for Business Card

Company name, employee name and title, work and cell phone numbers, email and website, and Contractor number.

our work scope should be on card somewhere: remodel ~ repair ~ service

logo or slight variation of logo also. (not necessarily set on keeping exact logo)

Colors

Designer to choose colors to be used in the design.

Requirements
Nice to have
• We deal with water so I think some sort of water element or just a color similar to pool water would be nice to integrate into design.

```html
<!DOCTYPE html>
<html lang="en">
<head>
<meta charset="utf-8">
<title>Bluecastle Aquatics – Business Card</title>
<link rel="stylesheet" href="https://fonts.googleapis.com/css2?family=Lato:wght@400;700&display=swap">
<style>
  :root {
    --bg: #d9dde2;
    --pool-deep: #0a67b8;
    --pool-mid: #0f86cf;
    --pool-light: #15a9e0;
    --stripe-red: #e0262f;
    --stripe-cyan: #19b3e6;
    --paper: #ffffff;
    --ink-white: #ffffff;
    --ink-blue: #1f86c8;
  }
  * { margin: 0; padding: 0; box-sizing: border-box; }
  html, body { width: 1200px; height: 1031px; overflow: hidden; background: var(--bg); }
  body { font-family: "Lato", sans-serif; }
  .canvas { position: relative; width: 1200px; height: 1031px; }

  .card {
    position: absolute;
    left: 190px;
    width: 820px;
    height: 469px;
    border-radius: 34px;
    overflow: hidden;
    box-shadow: 0 10px 26px rgba(0,0,0,.18);
  }
  .card--front { top: 31px; }
  .card--back { top: 531px; background: var(--paper); }

  .water-field {
    position: absolute; inset: 0;
    background:
      radial-gradient(ellipse at 30% 30%, rgba(90,210,245,.55), transparent 55%),
      radial-gradient(ellipse at 75% 75%, rgba(10,90,170,.5), transparent 60%),
      linear-gradient(160deg, var(--pool-light), var(--pool-mid) 55%, var(--pool-deep));
  }

  .company-name { font-family: "Lato", sans-serif; font-weight: 400; line-height: 1; white-space: nowrap; }
  .brand-dot { border-radius: 50%; flex: none; }

  .front-brand {
    position: absolute; top: 170px; left: 0; right: 0;
    display: flex; justify-content: center; align-items: center; gap: 18px;
    color: var(--ink-white);
  }
  .front-brand .company-name { font-size: 46px; }
  .front-brand .brand-dot { width: 46px; height: 46px; background: var(--ink-white); }

  .scope {
    position: absolute; top: 318px; left: 0; right: 0;
    display: flex; justify-content: center; align-items: center; gap: 20px;
    font-size: 28px; letter-spacing: .08em; color: var(--ink-white);
  }
  .scope__bullet { width: 14px; height: 14px; border-radius: 50%; border: 2px solid var(--ink-white); }

  .back-shape { position: absolute; inset: 0; width: 100%; height: 100%; }

  .back-brand {
    position: absolute; left: 40px; top: 212px; width: 330px;
    display: flex; justify-content: center; align-items: center; gap: 12px;
    color: var(--ink-blue);
  }
  .back-brand .company-name { font-size: 30px; }
  .back-brand .brand-dot { width: 32px; height: 32px; background: var(--ink-blue); }

  .contact {
    position: absolute; right: 48px; top: 58px; width: 360px;
    color: var(--ink-white); text-align: right;
  }
  .contact__name { font-size: 27px; letter-spacing: .06em; text-transform: uppercase; }
  .contact__title { font-size: 17px; margin-top: 4px; }
  .contact__list { list-style: none; margin-top: 50px; font-size: 17px; line-height: 1.55; }
  .contact__list li { display: flex; justify-content: flex-end; align-items: center; gap: 10px; }
  .contact__icon { width: 14px; height: 14px; flex: none; }
  .contact__license { margin-top: 22px; font-size: 21px; font-weight: 700; }
</style>
</head>
<body>
<main class="canvas">

  <section class="card card--front" aria-label="Business card front">
    <div class="water-field" role="img" aria-label="Pool water background with rising bubbles"></div>
    <div class="front-brand">
      <span class="brand-dot"></span>
      <span class="company-name">Bluecastle Aquatics</span>
    </div>
    <div class="scope">
      <span class="scope__bullet"></span><span>REMODEL</span>
      <span class="scope__bullet"></span><span>REPAIR</span>
      <span class="scope__bullet"></span><span>SERVICE</span>
    </div>
  </section>

  <section class="card card--back" aria-label="Business card back">
    <svg class="back-shape" viewBox="0 0 820 469" preserveAspectRatio="none" aria-hidden="true">
      <defs>
        <linearGradient id="panelBlue" x1="0" y1="0" x2="1" y2="1">
          <stop offset="0" stop-color="#1497dc"/>
          <stop offset="1" stop-color="#0a62b4"/>
        </linearGradient>
        <linearGradient id="paperFade" x1="0" y1="0" x2="1" y2="0">
          <stop offset="0" stop-color="#f3f4f6"/>
          <stop offset="1" stop-color="#ffffff"/>
        </linearGradient>
      </defs>
      <rect width="820" height="469" fill="url(#paperFade)"/>
      <path d="M330 0 C 420 120, 420 330, 360 469 L820 469 L820 0 Z" fill="var(--stripe-red)"/>
      <path d="M352 0 C 440 120, 440 330, 380 469 L820 469 L820 0 Z" fill="var(--stripe-cyan)"/>
      <path d="M368 0 C 456 120, 456 330, 396 469 L820 469 L820 0 Z" fill="url(#panelBlue)"/>
    </svg>

    <div class="back-brand">
      <span class="brand-dot"></span>
      <span class="company-name">Bluecastle Aquatics</span>
    </div>

    <div class="contact">
      <div class="contact__name">Daniel R. Hale</div>
      <div class="contact__title">CEO/Founder</div>
      <ul class="contact__list">
        <li>(904) 555-0182
          <svg class="contact__icon" viewBox="0 0 16 16"><path d="M4 1l3 3-2 2c1 2 3 4 5 5l2-2 3 3-2 3C7 15 1 9 1 3z" fill="#fff"/></svg>
        </li>
        <li>(904) 555-0247
          <svg class="contact__icon" viewBox="0 0 16 16"><rect x="4" y="1" width="8" height="14" rx="1.5" fill="none" stroke="#fff" stroke-width="1.6"/></svg>
        </li>
        <li>dhale@bluecastleaquatics.com
          <svg class="contact__icon" viewBox="0 0 16 16"><rect x="1" y="3" width="14" height="10" fill="none" stroke="#fff" stroke-width="1.6"/><path d="M1 3l7 6 7-6" fill="none" stroke="#fff" stroke-width="1.6"/></svg>
        </li>
        <li>www.bluecastleaquatics.com
          <svg class="contact__icon" viewBox="0 0 16 16"><circle cx="8" cy="8" r="6.5" fill="none" stroke="#fff" stroke-width="1.5"/><path d="M1.5 8h13M8 1.5c-3 3.5-3 9.5 0 13M8 1.5c3 3.5 3 9.5 0 13" fill="none" stroke="#fff" stroke-width="1.2"/></svg>
        </li>
      </ul>
      <div class="contact__license">Contractor No: CPC-1458203</div>
    </div>
  </section>

</main>
</body>
</html>
```